Business card design for a engineering company

I need a double sided business card design for my company "Verdmont Flow Solutions". The card will be used in Malaysia. Sleek and professional, with a little design flare to it.
Information to showcase:
1. Company logo
2. Name, title, phone, email address, website address
3. our products "Pumping technology, Valve & actuation, Air Moving Technology
Example:
Ravi Tanaka
Business manager
ravi.tanaka@verdmont-example.com
www.verdmont-example.com.my
- Pumping technology
- Valve & actuation
- Air moving technology
Target Market(s)
engineers, purchasing managers
Industry/Entity Type
Business
Contact Information for Business Card
Ravi Tanaka
Business manager
ravi.tanaka@verdmont-example.com
www.verdmont-example.com.my
- Pumping technology
- Valve & actuation
- Air moving technology
catch phrase : "Solving flow challenges, exceeding expectations"

```html
<!DOCTYPE html>
<html lang="en">
<head>
<meta charset="utf-8">
<title>Verdmont Flow Solutions – Business Card</title>
<link rel="stylesheet" href="https://fonts.googleapis.com/css2?family=Questrial&family=Arimo:wght@400;700&display=swap">
<style>
  :root {
    --bg: #e9e9e7;
    --paper: #f7f6f3;
    --orange: #c9700e;
    --orange-deep: #a85a08;
    --slate: #2f4450;
    --steel: #8fa1ab;
    --grey-text: #5e6b72;
    --cream: #f5e6cc;
    --ink: #111111;
  }
  * { margin: 0; padding: 0; box-sizing: border-box; }
  html, body { width: 1200px; height: 1000px; overflow: hidden; }
  body { background: var(--bg); position: relative; font-family: "Questrial", sans-serif; }

  .card {
    position: absolute;
    width: 560px;
    height: 320px;
    background: var(--paper);
    box-shadow: 0 3px 10px rgba(0,0,0,0.18);
    overflow: hidden;
  }
  .card--back { left: 560px; top: 130px; }
  .card--front { left: 90px; top: 540px; }

  /* Back side */
  .tagline {
    position: absolute; top: 22px; left: 0; width: 100%;
    text-align: center; font-variant: small-caps; letter-spacing: 1.5px;
    font-size: 17px; color: var(--grey-text);
  }
  .brand {
    position: absolute; display: flex; align-items: center; gap: 12px;
  }
  .brand__mark { background: var(--slate); }
  .brand__text { display: flex; flex-direction: column; line-height: 1; }
  .brand__name { color: var(--slate); letter-spacing: 2px; }
  .brand__sub { color: var(--slate); letter-spacing: 5px; text-transform: uppercase; }

  .card--back .brand { top: 58px; left: 130px; }
  .card--back .brand__mark { width: 40px; height: 40px; }
  .card--back .brand__name { font-size: 40px; }
  .card--back .brand__sub { font-size: 13px; margin-top: 3px; }

  .products-band {
    position: absolute; left: 0; top: 122px; width: 100%; height: 126px;
    background: linear-gradient(180deg, var(--orange) 0%, var(--orange-deep) 100%);
    display: flex; flex-direction: column; align-items: center; justify-content: center;
    padding-top: 40px;
  }
  .products { list-style: none; text-align: center; color: var(--cream); font-variant: small-caps; font-size: 19px; letter-spacing: 1px; line-height: 1.15; }
  .card--back .web {
    position: absolute; top: 258px; width: 100%; text-align: center;
    font-size: 17px; letter-spacing: 2.5px; color: var(--grey-text); text-transform: uppercase;
  }

  /* Front side */
  .front-art { position: absolute; inset: 0; }
  .card--front .brand { top: 18px; left: 24px; background: var(--paper); padding: 4px 8px; }
  .card--front .brand__mark { width: 22px; height: 22px; }
  .card--front .brand__name { font-size: 21px; letter-spacing: 1px; }
  .card--front .brand__sub { font-size: 8px; letter-spacing: 3px; margin-top: 2px; }

  .contact { position: absolute; left: 262px; top: 136px; font-family: "Arimo", sans-serif; color: var(--ink); white-space: nowrap; }
  .contact__name { font-size: 19px; font-weight: 700; }
  .contact__title { font-size: 15px; margin-top: 2px; }
  .contact__lines { margin-top: 26px; font-size: 15px; line-height: 1.35; font-family: "Questrial", sans-serif; }
</style>
</head>
<body>

  <section class="card card--back" aria-label="Business card, back">
    <p class="tagline">Solving flow challenges, exceeding expectations</p>
    <div class="products-band">
      <ul class="products">
        <li>Pumping technology</li>
        <li>Valve &amp; actuation</li>
        <li>Air moving technology</li>
      </ul>
    </div>
    <div class="brand">
      <span class="brand__mark"></span>
      <span class="brand__text">
        <span class="brand__name">VERDMONT</span>
        <span class="brand__sub">Flow Solutions</span>
      </span>
    </div>
    <p class="web">www.verdmont-example.com.my</p>
  </section>

  <section class="card card--front" aria-label="Business card, front">
    <svg class="front-art" width="560" height="320" viewBox="0 0 560 320" aria-hidden="true">
      <rect x="0" y="14" width="150" height="52" fill="var(--orange)"/>
      <polygon points="250,70 560,70 560,102 244,102" fill="var(--orange-deep)"/>
      <rect x="0" y="268" width="560" height="52" fill="var(--steel)"/>
      <polygon points="215,282 560,282 560,320 240,320" fill="var(--orange)"/>
    </svg>
    <div class="brand">
      <span class="brand__mark"></span>
      <span class="brand__text">
        <span class="brand__name">VERDMONT</span>
        <span class="brand__sub">Flow Solutions</span>
      </span>
    </div>
    <div class="contact">
      <p class="contact__name">Ravi Tanaka</p>
      <p class="contact__title">Business manager</p>
      <div class="contact__lines">
        <p>ravi.tanaka@verdmont-example.com</p>
        <p>www.verdmont-example.com.my</p>
      </div>
    </div>
  </section>

</body>
</html>
```